Flyer-Design für Jungwinzergruppe
Zielgruppe
Wir sind eine Jungwinzergruppe und produzieren unsere eigenen Weine und Sekte. Unsere Zielgruppe ist gemischt aus jungen und älteren Leuten.

```html
<!DOCTYPE html>
<html lang="de">
<head>
<meta charset="utf-8">
<title>Die Rebensprossen – Flyer</title>
<link rel="stylesheet" href="https://fonts.googleapis.com/css2?family=Jura:wght@400;500;600&family=Quicksand:wght@400;500&family=Courier+Prime:wght@700&display=swap">
<style>
  :root{
    --wine:#993246;
    --wine-dark:#7a2234;
    --wine-line:#c98a96;
    --paper:#f3f2f2;
    --ink:#4a4a4a;
    --white:#ffffff;
    --stage:#e8e8e8;
    --photo-a:#d9d9d9;
    --photo-b:#3a3a3a;
  }
  *{box-sizing:border-box;margin:0;padding:0}
  html,body{width:1200px;height:2325px;overflow:hidden;background:var(--stage)}
  body{position:relative;font-family:"Quicksand",sans-serif;color:var(--ink)}
  .spread{position:absolute;left:50px;width:1100px;height:778px;display:grid;grid-template-columns:367px 366px 367px;box-shadow:0 10px 30px rgba(0,0,0,.12)}
  .spread--outside{top:324px}
  .spread--inside{top:1222px}
  .panel{position:relative;overflow:hidden;height:778px}
  .panel--paper{background:var(--paper)}
  .panel--wine{background:var(--wine);color:var(--white)}
  .shape{position:absolute;left:0;top:0;display:block}
  .rule{height:1px;background:var(--wine);opacity:.7}
  .panel--wine .rule{background:var(--wine-line)}
  .title{font-family:"Jura",sans-serif;font-weight:500}
  .mono{font-family:"Courier Prime",monospace;font-weight:700}

  /* brand box */
  .brand-box{position:absolute;background:var(--white);width:46px;height:170px;display:flex;align-items:center;justify-content:center}
  .brand-box span{writing-mode:vertical-rl;transform:rotate(180deg);font-family:"Jura",sans-serif;font-weight:600;font-size:17px;letter-spacing:2px;color:var(--wine)}

  /* cover */
  .cover-title{position:absolute;top:302px;left:0;right:0;text-align:center;font-size:34px;color:var(--white)}
  .cover-rule{position:absolute;top:356px;left:40px;right:40px}
  .cover-tag{position:absolute;top:372px;left:0;right:0;text-align:center;font-family:"Jura",sans-serif;font-size:17px;letter-spacing:4px;color:var(--white)}
  .web-pill{position:absolute;left:50px;right:22px;bottom:34px;height:32px;border-radius:16px;background:var(--wine);color:var(--white);font-family:"Jura",sans-serif;font-size:14px;display:flex;align-items:center;justify-content:center;letter-spacing:.5px}

  /* back */
  .back-intro{position:absolute;top:244px;left:34px;right:34px;font-size:10.8px;line-height:1.55;text-align:justify}
  .back-head{position:absolute;top:425px;left:40px;right:40px}
  .back-head h2{font-family:"Jura",sans-serif;font-weight:500;font-size:24px;text-align:center;padding:10px 0 8px}
  .contact{position:absolute;top:520px;left:40px;right:40px}
  .contact-name{font-family:"Jura",sans-serif;font-size:20px;letter-spacing:3px;line-height:1.05}
  .contact-sub{font-family:"Jura",sans-serif;font-size:15px;letter-spacing:2.5px;margin-bottom:18px}
  .contact-line{display:flex;align-items:center;gap:9px;font-family:"Jura",sans-serif;font-size:11.5px;margin-bottom:6px}
  .social{position:absolute;right:40px;top:600px;display:flex;gap:10px}
  .social span{width:24px;height:24px;border:1.5px solid var(--white);border-radius:50%}

  /* flap */
  .flap-head{position:absolute;top:44px;left:28px;right:28px}
  .flap-head h2{font-size:25px;color:var(--wine);text-align:center;padding:8px 0 6px}
  .flap-sub{position:absolute;top:110px;left:28px;right:28px;font-size:12.5px;color:var(--wine);line-height:1.25}
  .flap-body{position:absolute;top:158px;left:28px;right:28px;font-size:10.3px;line-height:1.5;text-align:justify}
  .flap-body p{margin-bottom:7px}
  .flap-body strong{color:var(--wine)}

  /* inside left */
  .facts{position:absolute;top:210px;left:20px;right:20px;display:flex;justify-content:space-between}
  .fact{width:100px;text-align:center}
  .fact-num{width:30px;height:30px;border-radius:50%;background:var(--wine);color:var(--white);border:2px solid var(--white);box-shadow:0 0 0 1.5px var(--wine);margin:0 auto 6px;display:flex;align-items:center;justify-content:center;font-family:"Jura",sans-serif;font-size:15px}
  .fact-label{font-family:"Jura",sans-serif;font-size:12.5px;color:var(--wine);line-height:1.1}
  .wines{position:absolute;top:300px;left:28px;right:28px}
  .wine h3{font-family:"Jura",sans-serif;font-weight:500;font-size:18px;color:var(--wine);margin-bottom:4px}
  .wine h4{font-family:"Jura",sans-serif;font-weight:600;font-size:11px;color:var(--wine);letter-spacing:1px}
  .wine p{font-size:10.5px;line-height:1.5;margin-bottom:16px;text-align:justify}

  /* team */
  .team-head{position:absolute;top:22px;left:40px;right:40px}
  .team-head h2{font-size:21px;text-align:center;padding:8px 0 6px}
  .portraits{position:absolute;top:100px;left:0;right:0;display:flex;flex-direction:column;align-items:center;gap:22px}
  .member{text-align:center}
  .member svg{display:block;margin:0 auto 8px}
  .member-name{font-family:"Jura",sans-serif;font-size:14px;padding-bottom:4px;border-bottom:1px solid var(--wine-line);display:inline-block;min-width:120px}

  /* bios */
  .bios{position:absolute;top:26px;left:30px;right:30px}
  .bio{margin-bottom:26px}
  .bio h3{font-size:20px;color:var(--wine);text-align:center;padding:6px 0 5px}
  .bio p{font-size:10.3px;line-height:1.45;margin-top:10px}
</style>
</head>
<body>

<!-- Outside of the folder -->
<section class="spread spread--outside">

  <!-- inner flap -->
  <article class="panel panel--paper">
    <header class="flap-head">
      <div class="rule"></div>
      <h2 class="title">Die Rebensprossen</h2>
      <div class="rule"></div>
    </header>
    <p class="flap-sub mono">Junge Reben! – Drei junge Winzer – drei Philosophien – eine Leidenschaft</p>
    <div class="flap-body">
      <p>Angefangen hat es im Jahr 2013. Die drei Jungs von der Ahr – Tim Ossenberg, Jonas Wendler und Lukas Brennholt – steckten mitten in ihrer Ausbildung zum Winzer. Schon damals war für sie klar, dass der Weinbau mehr als nur ihr Beruf sein würde. Sie hatten eigene Ideen und wollten zeigen, was in ihnen steckt.</p>
      <p>Sie taten sich zusammen und nannten sich fortan <strong>DIE REBENSPROSSEN</strong>, so steht es auch auf den recht außergewöhnlichen Etiketten ihrer Weinflaschen. Überhaupt zeigen schon ihre Etiketten, dass sie mit frischen Ideen an die Sache herangehen.</p>
      <p>Im ersten Schritt haben sie einen kleinen Weinberg mit alten Spätburgunder-Reben gepachtet, später kamen weitere Parzellen in Steillage dazu. Gemeinsam bewirtschaften sie inzwischen rund 3.500 m² Rebfläche.</p>
      <p>Den drei Jungwinzern geht es in erster Linie darum, durch neue, moderne und jüngere Interpretationen sowohl im Anbau als auch im Ausbau ihrer Weine einen eigenen Stil zu entwickeln. Dabei ergänzen sie die gute Tradition mit frischen Ideen und erzeugen so jährlich rund 2.500 Flaschen Wein und Sekt.</p>
    </div>
    <svg class="shape" width="367" height="778" viewBox="0 0 367 778" aria-hidden="true">
      <path d="M0 648 Q170 590 367 572 V590 Q170 606 0 664 Z" fill="var(--wine)"/>
    </svg>
    <svg class="shape" width="367" height="778" viewBox="0 0 367 778" role="img" aria-label="Foto: die drei Jungwinzer sitzen mit Weinflaschen vor einer Bruchsteinmauer">
      <defs><linearGradient id="g-flap" x1="0" y1="0" x2="1" y2="1"><stop offset="0" stop-color="#8a8074"/><stop offset="1" stop-color="#2d2a2a"/></linearGradient></defs>
      <path d="M0 664 Q170 606 367 590 V778 H0 Z" fill="url(#g-flap)"/>
    </svg>
  </article>

  <!-- back panel -->
  <article class="panel panel--wine">
    <svg class="shape" width="366" height="240" viewBox="0 0 366 240" role="img" aria-label="Schwarzweißfoto: zwei Jungwinzer am Weinfass">
      <defs><linearGradient id="g-back" x1="0" y1="0" x2="1" y2="1"><stop offset="0" stop-color="var(--photo-a)"/><stop offset="1" stop-color="var(--photo-b)"/></linearGradient></defs>
      <circle cx="196" cy="112" r="92" fill="var(--white)"/>
      <circle cx="196" cy="112" r="87" fill="url(#g-back)"/>
    </svg>
    <div class="brand-box" style="left:72px;top:10px"><span>Rebensprossen</span></div>
    <p class="back-intro">2013 gründeten wir, 3 Freunde von der Ahr, die gemeinsam die Ausbildung absolvierten, unser Jungwinzerprojekt, um unsere eigenen Ideen und Vorstellungen in Form eines Weines zu verwirklichen. Durch neue und jüngere Interpretationen des Anbaus und Ausbaus bildete sich unser eigener Stil. Diesen versuchen wir nun weiterzuentwickeln, um einen Wein nach unseren eigenen Vorstellungen zu machen. Dabei versuchen wir die Tradition mit frischen Ideen zu ergänzen.</p>
    <div class="back-head">
      <div class="rule"></div>
      <h2>Ihr Weg zu uns</h2>
      <div class="rule"></div>
    </div>
    <div class="contact">
      <div class="contact-name">Die Rebensprossen</div>
      <div class="contact-sub">junge Weine von der Ahr</div>
      <div class="contact-line">
        <svg width="10" height="13" viewBox="0 0 10 13" aria-hidden="true"><path d="M5 0a5 5 0 0 1 5 5c0 3.5-5 8-5 8S0 8.5 0 5a5 5 0 0 1 5-5z" fill="var(--white)"/><circle cx="5" cy="5" r="1.8" fill="var(--wine)"/></svg>
        Kelterweg 12 | 53901 Rebenhausen
      </div>
      <div class="contact-line">
        <svg width="12" height="9" viewBox="0 0 12 9" aria-hidden="true"><rect width="12" height="9" rx="1" fill="var(--white)"/><path d="M0.5 0.8 6 5 11.5 0.8" stroke="var(--wine)" fill="none"/></svg>
        info@rebensprossen-weine.de
      </div>
      <div class="contact-line">
        <svg width="12" height="12" viewBox="0 0 12 12" aria-hidden="true"><circle cx="6" cy="6" r="5.3" fill="none" stroke="var(--white)" stroke-width="1.2"/><ellipse cx="6" cy="6" rx="2.3" ry="5.3" fill="none" stroke="var(--white)"/><path d="M0.7 6H11.3" stroke="var(--white)"/></svg>
        www.rebensprossen-weine.de
      </div>
    </div>
    <div class="social" aria-label="Soziale Netzwerke"><span></span><span></span></div>
  </article>

  <!-- front cover -->
  <article class="panel panel--wine">
    <svg class="shape" width="367" height="290" viewBox="0 0 367 290" role="img" aria-label="Schwarzweißfoto: die drei Jungwinzer nebeneinander im Weinberg">
      <defs><linearGradient id="g-cover-top" x1="0" y1="0" x2="1" y2="1"><stop offset="0" stop-color="#cfcfcf"/><stop offset=".6" stop-color="#5a5a5a"/><stop offset="1" stop-color="#1e1e1e"/></linearGradient></defs>
      <path d="M0 0 H367 V150 C310 215 160 250 0 262 Z" fill="url(#g-cover-top)"/>
    </svg>
    <div class="brand-box" style="right:26px;top:88px"><span>Rebensprossen</span></div>
    <h1 class="cover-title title">Die Rebensprossen</h1>
    <div class="cover-rule rule"></div>
    <p class="cover-tag">Junge Weine von der Ahr!</p>
    <svg class="shape" width="367" height="778" viewBox="0 0 367 778" role="img" aria-label="Schwarzweißfoto: die drei Jungwinzer mit verschränkten Armen vor einer Steinmauer">
      <defs><linearGradient id="g-cover-bottom" x1="0" y1="0" x2="1" y2="1"><stop offset="0" stop-color="#9a9a9a"/><stop offset="1" stop-color="#262626"/></linearGradient></defs>
      <path d="M0 778 V640 Q30 560 190 548 Q330 548 367 620 V778 Z" fill="url(#g-cover-bottom)"/>
    </svg>
    <div class="web-pill">www.rebensprossen-weine.de</div>
  </article>
</section>

<!-- Inside of the folder -->
<section class="spread spread--inside">

  <!-- wines -->
  <article class="panel panel--paper">
    <svg class="shape" width="367" height="200" viewBox="0 0 367 200" role="img" aria-label="Foto: Weinflaschen mit eigenen Etiketten, Weinglas und Korken auf einem Holztisch">
      <defs><linearGradient id="g-bottles" x1="0" y1="0" x2="1" y2="1"><stop offset="0" stop-color="#6d5a44"/><stop offset=".5" stop-color="#3b2a26"/><stop offset="1" stop-color="#b49d7c"/></linearGradient></defs>
      <path d="M0 0 H367 V118 Q220 190 0 170 Z" fill="url(#g-bottles)"/>
      <path d="M0 170 Q220 190 367 118 V132 Q220 204 0 184 Z" fill="var(--wine)"/>
    </svg>
    <div class="facts">
      <div class="fact"><div class="fact-num">3</div><div class="fact-label">verschiedene Philosophien</div></div>
      <div class="fact"><div class="fact-num">3</div><div class="fact-label">junge Winzer</div></div>
      <div class="fact"><div class="fact-num">1</div><div class="fact-label">gemeinsame Leidenschaft</div></div>
    </div>
    <div class="wines">
      <div class="wine">
        <h3>Blanc de Noir trocken</h3>
        <h4>CHARAKTERISIERUNG:</h4>
        <p>Eleganter Blanc de Noir aus 100 % Spätburgunder-Trauben. Er zeichnet sich durch eine hohe Fruchtigkeit und frische Aromen aus. Da die Trauben auf Schiefer wachsen, erhält der Wein eine feine mineralische Note. Abgerundet wird das Ganze durch eine kurze Lagerung im Eichenholzfass.</p>
      </div>
      <div class="wine">
        <h3>Spätburgunder trocken</h3>
        <h4>CHARAKTERISIERUNG:</h4>
        <p>Typischer Ahr-Burgunder, der ausschließlich in Steillagen auf Schieferverwitterungsgestein gewachsen ist. Die Eleganz und Komplexität wird erreicht durch niedrige Erträge, selektive Lese und den anschließenden Ausbau sowie der Lagerung in kleinen, neuen Eichenholzfässern.</p>
      </div>
    </div>
  </article>

  <!-- team -->
  <article class="panel panel--wine">
    <header class="team-head">
      <div class="rule"></div>
      <h2 class="title">Die Rebensprossen</h2>
      <div class="rule"></div>
    </header>
    <div class="portraits">
      <div class="member">
        <svg width="124" height="124" viewBox="0 0 124 124" role="img" aria-label="Schwarzweißporträt von Jonas Wendler">
          <defs><linearGradient id="g-p1" x1="0" y1="0" x2="1" y2="1"><stop offset="0" stop-color="var(--photo-a)"/><stop offset="1" stop-color="var(--photo-b)"/></linearGradient></defs>
          <circle cx="62" cy="62" r="62" fill="var(--white)"/><circle cx="62" cy="62" r="58" fill="url(#g-p1)"/>
        </svg>
        <span class="member-name">Jonas Wendler</span>
      </div>
      <div class="member">
        <svg width="124" height="124" viewBox="0 0 124 124" role="img" aria-label="Schwarzweißporträt von Lukas Brennholt">
          <defs><linearGradient id="g-p2" x1="0" y1="0" x2="1" y2="1"><stop offset="0" stop-color="#c4c4c4"/><stop offset="1" stop-color="#2f2f2f"/></linearGradient></defs>
          <circle cx="62" cy="62" r="62" fill="var(--white)"/><circle cx="62" cy="62" r="58" fill="url(#g-p2)"/>
        </svg>
        <span class="member-name">Lukas Brennholt</span>
      </div>
      <div class="member">
        <svg width="124" height="124" viewBox="0 0 124 124" role="img" aria-label="Foto von Tim Ossenberg bei der Arbeit an jungen Reben">
          <defs><linearGradient id="g-p3" x1="0" y1="0" x2="1" y2="1"><stop offset="0" stop-color="#b9c2a4"/><stop offset="1" stop-color="#2e2e2a"/></linearGradient></defs>
          <circle cx="62" cy="62" r="62" fill="var(--white)"/><circle cx="62" cy="62" r="58" fill="url(#g-p3)"/>
        </svg>
        <span class="member-name">Tim Ossenberg</span>
      </div>
    </div>
  </article>

  <!-- bios -->
  <article class="panel panel--paper">
    <div class="bios">
      <section class="bio">
        <div class="rule"></div>
        <h3 class="title">Jonas Wendler</h3>
        <div class="rule"></div>
        <p>Jonas absolvierte seine Ausbildung zum Winzer von 2012–2015 beim Weingut Hallerberg. Von 2015 bis 2016 machte er sein Fachabitur für Agrarwirtschaft.</p>
        <p>Seitdem ist er als Winzer in einem Weingut im Tal angestellt und sammelt wichtige Erfahrungen. Nebenbei macht er die Ausbildung zum Winzermeister.</p>
        <p>Zum Weinbau ist er durch seinen Opa gekommen, der Jahrzehnte als Genossenschaftswinzer gearbeitet hat.</p>
      </section>
      <section class="bio">
        <div class="rule"></div>
        <h3 class="title">Lukas Brennholt</h3>
        <div class="rule"></div>
        <p>Lukas absolvierte seine Ausbildung zum Winzer von 2012–2015 beim Weingut Sonnhang.</p>
        <p>Von 2015 bis 2016 machte er sein Fachabitur für Agrarwirtschaft. Seit Herbst 2016 studiert er Weinbau und Oenologie an der Hochschule.</p>
        <p>Weinbau wird in der Familie Brennholt in der fünften Generation betrieben. So ist es naheliegend, dass er in Zukunft ins elterliche Weingut einsteigen wird.</p>
      </section>
      <section class="bio">
        <div class="rule"></div>
        <h3 class="title">Tim Ossenberg</h3>
        <div class="rule"></div>
        <p>Tim absolvierte seine Ausbildung zum Winzer von 2012–2015 beim Weingut Lindenhof und beim Winzerverein Talblick.</p>
        <p>Von 2015 bis 2016 machte er sein Fachabitur für Agrarwirtschaft. Seit Herbst 2016 studiert er Weinbau und Oenologie an der Hochschule.</p>
        <p>Zum Weinbau ist er durch seinen Onkel gekommen, der Kellermeister in einem der größten Weingüter der Ahr ist.</p>
      </section>
    </div>
  </article>
</section>

</body>
</html>
```